Vorra Fleet business card

I am needing a business card that at a glance shows all the services that we provide emphasizing some more than others. We are a Fleet and Compliance management company as well as a software company. We provide outsourced solutions for PXM compliance and HR services via our own software.
In addition, we do
drug testing
GPS
Cameras
Electronic DVIRS
ELD's

Target Market(s)

Transportation company owners

Industry/Entity Type

Transportation supplier

Contact Information for Business Card

the card should inform potential customers what we do

Other font styles liked:
• I have added brand guidelines. See attached

Requirements
Must have
• See description
Should not have
• Colors outside my brand guide. See attached

```html
<!DOCTYPE html>
<html lang="en">
<head>
<meta charset="utf-8">
<title>Vorra Fleet Business Card</title>
<link rel="stylesheet" href="https://fonts.googleapis.com/css2?family=Open+Sans:wght@400;600;700&display=swap">
<style>
  :root {
    --stage: #3b3b3b;
    --card-white: #ffffff;
    --card-black: #1c1c1c;
    --brand-red: #e8282e;
    --ink: #1a1a1a;
    --muted: #555555;
    --light: #f2f2f2;
  }
  * { margin: 0; padding: 0; box-sizing: border-box; }
  html, body { width: 1200px; height: 801px; overflow: hidden; }
  body {
    background: var(--stage);
    font-family: "Open Sans", Arial, sans-serif;
    position: relative;
  }
  .card {
    position: absolute;
    width: 500px;
    height: 286px;
    border-bottom: 4px solid var(--brand-red);
  }
  .card-front { left: 70px; top: 90px; background: var(--card-white); }
  .card-back  { left: 630px; top: 425px; background: var(--card-black); border: 1px solid var(--brand-red); border-bottom-width: 4px; }

  .wordmark {
    display: flex; align-items: center; gap: 10px;
    font-weight: 700; letter-spacing: 0.02em; line-height: 1;
  }
  .wordmark-mark { width: 16px; height: 16px; background: var(--brand-red); }
  .card-front .wordmark { position: absolute; left: 34px; top: 40px; font-size: 34px; color: var(--ink); }

  .person { position: absolute; right: 34px; top: 40px; text-align: right; }
  .person-name { color: var(--brand-red); font-weight: 700; font-size: 19px; letter-spacing: 0.01em; }
  .person-title { color: var(--muted); font-size: 13px; margin-top: 2px; }
  .rule-top { position: absolute; right: 34px; top: 100px; width: 250px; height: 1px; background: var(--brand-red); }

  .rule-bottom { position: absolute; left: 34px; top: 188px; width: 250px; height: 1px; background: var(--brand-red); }
  .contact { position: absolute; left: 34px; top: 200px; list-style: none; font-size: 14px; color: var(--ink); }
  .contact li { display: flex; align-items: center; gap: 8px; line-height: 22px; }
  .contact svg { width: 12px; height: 12px; fill: var(--brand-red); flex: none; }

  .card-back .wordmark {
    position: absolute; left: 0; right: 0; top: 92px; justify-content: center;
    font-size: 48px; color: var(--light);
  }
  .services {
    position: absolute; left: 0; right: 0; bottom: 28px;
    display: flex; justify-content: center; align-items: center; gap: 10px;
    list-style: none; color: var(--light); font-size: 14px;
  }
  .services li + li::before {
    content: ""; display: inline-block; width: 5px; height: 5px; border-radius: 50%;
    background: var(--brand-red); margin-right: 10px; vertical-align: middle;
  }
</style>
</head>
<body>
  <section class="card card-front">
    <div class="wordmark"><span class="wordmark-mark"></span>Vorra Fleet</div>
    <div class="person">
      <p class="person-name">DANA KORVEL</p>
      <p class="person-title">President</p>
    </div>
    <div class="rule-top"></div>
    <div class="rule-bottom"></div>
    <ul class="contact">
      <li><svg viewBox="0 0 24 24"><path d="M6.6 10.8a15 15 0 0 0 6.6 6.6l2.2-2.2a1 1 0 0 1 1-.25 11.4 11.4 0 0 0 3.6.57 1 1 0 0 1 1 1V20a1 1 0 0 1-1 1A17 17 0 0 1 3 4a1 1 0 0 1 1-1h3.5a1 1 0 0 1 1 1c0 1.25.2 2.45.57 3.57a1 1 0 0 1-.25 1z"/></svg>555-014-2290</li>
      <li><svg viewBox="0 0 24 24"><path d="M2 5h20v14H2zm2 2v.5l8 5 8-5V7l-8 5z"/></svg>info@vorrafleet.com</li>
      <li><svg viewBox="0 0 24 24"><circle cx="12" cy="12" r="10"/></svg>www.vorrafleet.com</li>
    </ul>
  </section>

  <section class="card card-back">
    <div class="wordmark"><span class="wordmark-mark"></span>Vorra Fleet</div>
    <ul class="services">
      <li>Drug Testing</li>
      <li>GPS</li>
      <li>Cameras</li>
      <li>Electronic DVIRS</li>
      <li>ELD's</li>
    </ul>
  </section>
</body>
</html>
```